Poster Design Project

Need a design for a music festival called Counter-Lanternweek

The design needs to have areas for the following:
- Band Names
- DJ Names
- Sponsor Names and Logos
- Event location, Date & Time

Industry/Entity Type

Festival

```html
<!DOCTYPE html>
<html lang="en">
<head>
<meta charset="utf-8">
<title>Counter-Lanternweek Music Festival Poster</title>
<link rel="stylesheet" href="https://fonts.googleapis.com/css2?family=Alfa+Slab+One&family=PT+Sans+Narrow:wght@400;700&family=Roboto+Slab:wght@700;800&display=swap">
<style>
  :root {
    --ink: #231f20;
    --cream: #f7f2e1;
    --cream-text: #f5ecd3;
    --wood-light: #c99d66;
    --wood-mid: #a8743f;
    --wood-dark: #7a4f27;
    --page: #ffffff;
  }
  * { margin: 0; padding: 0; box-sizing: border-box; }
  html, body { width: 1200px; height: 1200px; overflow: hidden; background: var(--page); }
  .poster {
    position: absolute; left: 175px; top: 0; width: 851px; height: 1200px;
    overflow: hidden; font-family: "PT Sans Narrow", "Arial Narrow", sans-serif;
  }
  .wood {
    position: absolute; inset: 0;
    background:
      radial-gradient(ellipse at 60% 55%, rgba(255,220,170,.25), transparent 60%),
      linear-gradient(160deg, var(--wood-mid) 0%, var(--wood-light) 35%, var(--wood-mid) 60%, var(--wood-dark) 100%);
  }
  .deco { position: absolute; }
  .deco--drums { left: 38px; top: 87px; width: 141px; height: 102px; background: rgba(247,242,225,.35); border-radius: 14px; }
  .deco--notes { left: 538px; top: 266px; width: 313px; height: 166px; background: rgba(247,242,225,.35); border-radius: 20px; }
  .deco--guitar-line { left: 659px; top: 663px; width: 115px; height: 295px; background: rgba(35,31,32,.18); border-radius: 40px; }
  .deco--guitar-solid { left: 326px; top: 860px; width: 540px; height: 360px; background: var(--ink); border-radius: 160px 0 0 60px; }

  .dates { position: absolute; left: 0; right: 0; top: 60px; text-align: center; color: var(--cream-text); }
  .dates__days { font-weight: 700; font-size: 34px; line-height: 1; }
  .dates__time { font-weight: 700; font-size: 21px; margin-top: 8px; }

  .title-band {
    position: absolute; left: -60px; top: 150px; width: 980px; height: 166px;
    background: var(--ink); transform: rotate(-5deg); transform-origin: center;
    color: var(--cream-text); text-align: center; padding-top: 22px;
  }
  .title-band__name { font-family: "Alfa Slab One", Georgia, serif; font-size: 62px; line-height: 1.05; letter-spacing: 1px; }
  .title-band__cause { font-weight: 700; font-size: 25px; margin-top: 6px; }

  .charity-mark {
    position: absolute; left: 371px; top: 330px; width: 134px; height: 70px;
    background: #fff; display: flex; align-items: center; justify-content: center; gap: 6px;
    color: var(--ink); font-weight: 700; font-size: 17px;
  }
  .charity-mark__square { width: 14px; height: 14px; background: var(--ink); }

  .events {
    position: absolute; left: 93px; top: 371px; width: 820px; height: 420px;
    background: var(--cream); transform: rotate(5deg); transform-origin: top left;
  }
  .events__head { background: var(--ink); color: var(--cream-text); font-weight: 700; font-size: 25px; height: 40px; padding: 4px 24px; }
  .events__intro { width: 700px; margin-top: 14px; text-align: center; font-size: 23px; line-height: 1.18; color: var(--ink); }

  .lineup {
    position: absolute; list-style: none; text-align: center; color: var(--ink);
    font-family: "Roboto Slab", Georgia, serif; font-weight: 800; font-size: 19px; line-height: 27.5px; width: 260px;
  }
  .lineup--day-one { left: 126px; top: 568px; }
  .lineup--day-two { left: 408px; top: 584px; }

  .tickets {
    position: absolute; left: 42px; top: 812px; width: 312px; height: 148px;
    background: var(--cream); transform: rotate(-4deg); transform-origin: top left; color: var(--ink);
  }
  .tickets__head { background: var(--ink); color: var(--cream-text); font-weight: 700; font-size: 24px; height: 38px; padding: 3px 14px; }
  .tickets__body { padding: 8px 18px; font-size: 22px; line-height: 1.2; }

  .venue { position: absolute; left: 61px; top: 1004px; color: var(--cream-text); font-weight: 700; font-size: 23px; line-height: 39px; }
  .sponsors { position: absolute; left: 61px; top: 1138px; width: 265px; color: var(--cream-text); font-weight: 700; font-size: 12.5px; line-height: 1.5; }
</style>
</head>
<body>
<main class="poster">
  <div class="wood" role="img" aria-label="Cut tree trunk wood grain background"></div>
  <div class="deco deco--drums" role="img" aria-label="Line drawing of a drum kit"></div>
  <div class="deco deco--notes" role="img" aria-label="Cream music notes"></div>
  <div class="deco deco--guitar-line" role="img" aria-label="Line drawing of an electric guitar"></div>
  <div class="deco deco--guitar-solid" role="img" aria-label="Black guitar silhouette with stars and a vinyl record"></div>

  <header class="dates">
    <p class="dates__days">Saturday 23rd - Sunday 24th October</p>
    <p class="dates__time">11.00am - Late</p>
  </header>

  <section class="title-band">
    <h1 class="title-band__name">Counter-Lanternweek</h1>
    <p class="title-band__cause">Music Festival in aid of the local charity Cots for Cubs</p>
  </section>

  <div class="charity-mark"><span class="charity-mark__square"></span>Cots for Cubs</div>

  <section class="events">
    <h2 class="events__head">List of events</h2>
    <p class="events__intro">Over the festival you will enjoy: live music from a selection of band and Dj’s, raffles, games as well as food &amp; drink</p>
  </section>

  <ul class="lineup lineup--day-one">
    <li>Quiet Parish</li><li>Odd Physics</li><li>Crane &amp; Holt Company</li><li>The GreyFoxes</li>
    <li>Clara Whitby</li><li>Jolly Rascal</li><li>Moth Lantern</li><li>The Proven</li>
  </ul>
  <ul class="lineup lineup--day-two">
    <li>Quiet Parish</li><li>Odd Physics</li><li>Crane &amp; Holt Company</li><li>The GreyFoxes</li>
    <li>Clara Whitby</li><li>Jolly Rascal</li><li>Moth Lantern</li><li>The Proven</li>
  </ul>

  <section class="tickets">
    <h2 class="tickets__head">Tickets</h2>
    <div class="tickets__body">
      <p>Adults: $xx&nbsp; Children: $xx</p>
      <p>Call xxxxxxxxxxxxxx</p>
      <p>visit: xxxxxxxxxxxxxxxxx</p>
    </div>
  </section>

  <address class="venue" style="font-style:normal">
    To be held at<br>512 W. 48th St,<br>Riverton, NC 28999
  </address>

  <p class="sponsors">Sponsored by “hearthesound”, Kestrel Brewing Company, and Millrace Brewing Company</p>
</main>
</body>
</html>
```